Make an Awesome Graphic for a PPT

Attached is the specific content for the project. the X-factor of Adoption. It does not need a title just take the existing graphic an improve it. Attached is our company logo for color palette and the "ugly version". It should look modern and edge in terms of effect and font. Need it by Monday March 7th

```html
<!DOCTYPE html>
<html lang="en">
<head>
<meta charset="utf-8">
<title>The X-Factor of Adoption</title>
<link rel="stylesheet" href="https://fonts.googleapis.com/css2?family=Audiowide&display=swap">
<style>
  :root {
    --canvas-bg: #ffffff;
    --steel-light: #e3e5ea;
    --steel-mid: #b4b9c3;
    --steel-dark: #868c98;
    --steel-edge: #737986;
    --guide-line: #c4c8d2;
    --guide-line-blue: #9aa6bc;
    --label-blue: #2b3597;
    --label-blue-deep: #1a2270;
    --hub-light: #3f6fd6;
    --hub-mid: #1f46b0;
    --hub-deep: #102a78;
    --hub-rim: #5c8ee0;
    --hub-text: #c9ccd4;
    --hub-text-edge: #3a3f4d;
  }
  html, body {
    margin: 0;
    padding: 0;
    width: 1200px;
    height: 1200px;
    overflow: hidden;
    background: var(--canvas-bg);
  }
  .canvas {
    width: 1200px;
    height: 1200px;
    position: relative;
  }
  .adoption-diagram {
    display: block;
    width: 1200px;
    height: 1200px;
  }
  .arm-plate {
    fill: url(#steelGradient);
    stroke: var(--steel-edge);
    stroke-width: 2;
    filter: drop-shadow(0 4px 6px rgba(40, 45, 60, 0.35));
  }
  .arm-guide { stroke: var(--guide-line); stroke-width: 2; fill: none; }
  .arm-guide--blue { stroke: var(--guide-line-blue); }
  .arm-label {
    font-family: "Audiowide", sans-serif;
    font-size: 33px;
    letter-spacing: 2px;
    fill: var(--label-blue);
    stroke: var(--label-blue-deep);
    stroke-width: 0.6;
    text-anchor: middle;
  }
  .hub-tab { fill: var(--hub-mid); stroke: var(--hub-deep); stroke-width: 1.5; }
  .hub-disc {
    fill: url(#hubGradient);
    stroke: var(--hub-rim);
    stroke-width: 5;
    filter: drop-shadow(0 6px 10px rgba(10, 30, 90, 0.45));
  }
  .hub-label {
    font-family: "Audiowide", sans-serif;
    font-size: 44px;
    fill: var(--hub-text);
    stroke: var(--hub-text-edge);
    stroke-width: 1.2;
    paint-order: stroke;
    text-anchor: middle;
    letter-spacing: 1px;
  }
</style>
</head>
<body>
<main class="canvas">
  <svg class="adoption-diagram" viewBox="0 0 1000 1000" role="img" aria-label="The X-factor of adoption: farmer experience, farmer sentiment and innovation concept meet in the adoption zone">
    <defs>
      <linearGradient id="steelGradient" x1="0" y1="0" x2="1" y2="1">
        <stop offset="0" stop-color="var(--steel-light)"/>
        <stop offset="0.45" stop-color="var(--steel-mid)"/>
        <stop offset="1" stop-color="var(--steel-dark)"/>
      </linearGradient>
      <radialGradient id="hubGradient" cx="0.4" cy="0.3" r="0.8">
        <stop offset="0" stop-color="var(--hub-light)"/>
        <stop offset="0.55" stop-color="var(--hub-mid)"/>
        <stop offset="1" stop-color="var(--hub-deep)"/>
      </radialGradient>
      <g id="arm">
        <line class="arm-guide" x1="105" y1="126" x2="240" y2="126"/>
        <line class="arm-guide" x1="270" y1="140" x2="470" y2="340"/>
        <line class="arm-guide arm-guide--blue" x1="285" y1="140" x2="478" y2="333"/>
        <line class="arm-guide" x1="180" y1="258" x2="350" y2="428"/>
        <line class="arm-guide arm-guide--blue" x1="180" y1="275" x2="340" y2="435"/>
        <polygon class="arm-plate" points="120,140 240,140 520,420 420,520 90,190 88,178"/>
      </g>
    </defs>

    <g class="arm arm--top-left"><use href="#arm"/></g>
    <g class="arm arm--top-right" transform="translate(1000 0) scale(-1 1)"><use href="#arm"/></g>
    <g class="arm arm--bottom-left" transform="translate(0 1000) scale(1 -1)"><use href="#arm"/></g>
    <g class="arm arm--bottom-right" transform="translate(1000 1000) scale(-1 -1)"><use href="#arm"/></g>

    <text class="arm-label" transform="translate(275 300) rotate(45)">
      <tspan x="0" y="-8">FARMER</tspan>
      <tspan x="0" y="30">EXPERIENCE</tspan>
    </text>
    <text class="arm-label" transform="translate(690 290) rotate(-45)">
      <tspan x="0" y="-8">INNOVATION</tspan>
      <tspan x="0" y="30">CONCEPT</tspan>
    </text>
    <text class="arm-label" transform="translate(270 715) rotate(-45)">
      <tspan x="0" y="-8">INNOVATION</tspan>
      <tspan x="0" y="30">CONCEPT</tspan>
    </text>
    <text class="arm-label" transform="translate(700 725) rotate(45)">
      <tspan x="0" y="-8">FARMER</tspan>
      <tspan x="0" y="30">SENTIMENT</tspan>
    </text>

    <g class="hub">
      <polygon class="hub-tab" points="330,490 360,482 360,515 326,515 318,505"/>
      <polygon class="hub-tab" points="640,482 672,478 684,492 672,505 640,508"/>
      <circle class="hub-disc" cx="500" cy="500" r="148"/>
      <text class="hub-label" x="500" y="490">ADOPTION</text>
      <text class="hub-label" x="500" y="545">ZONE</text>
    </g>
  </svg>
</main>
</body>
</html>
```